Business Card Design Project

We are a commercial talent casting company, a very "now" company. We need a new business card that is both current, graphic and elegantly interesting. As we are a service business,
we need something that will attract the attention of new clients,
yet project a business that is 25 years old.

Industry/Entity Type

Business

Requirements
Must have
• 1. Logo - Nora Quillan Casting
2. Address - 47 Thornbury Street
New York, New York 10010
3. Phone - 212-738-4192
4. E-Mail - Casting@noraquillan.example

Nice to have
• Would like the card in black and white with the only accent
color being red.

```html
<!DOCTYPE html>
<html lang="en">
<head>
<meta charset="utf-8">
<title>Nora Quillan Casting – Business Card</title>
<link rel="stylesheet" href="https://fonts.googleapis.com/css2?family=Noto+Sans+Mono:wght@300;400&family=Roboto+Condensed:wght@700&display=swap">
<style>
  :root {
    --backdrop: #e4e4e2;
    --card: #0f0f0f;
    --ink: #f2f2f2;
    --ink-soft: #bdbdbd;
    --accent: #c8201f;
    --rule-soft: #8a8a8a;
  }
  * { margin: 0; padding: 0; box-sizing: border-box; }
  html, body {
    width: 1200px;
    height: 900px;
    overflow: hidden;
    background: var(--backdrop);
  }
  .stage {
    position: relative;
    width: 1200px;
    height: 900px;
  }
  .card {
    position: absolute;
    left: 365px;
    top: 50px;
    width: 470px;
    height: 800px;
    background: var(--card);
    box-shadow: 0 6px 24px rgba(0,0,0,0.25);
    overflow: hidden;
    font-family: "Noto Sans Mono", monospace;
    color: var(--ink);
  }
  .brand {
    position: absolute;
    right: 28px;
    top: 88px;
    font-family: "Roboto Condensed", sans-serif;
    font-weight: 700;
    font-size: 26px;
    letter-spacing: 0.2px;
    color: var(--ink);
    white-space: nowrap;
  }
  .brand-rules {
    position: absolute;
    left: 143px;
    top: 119px;
  }
  .holder {
    position: absolute;
    left: 0;
    right: 0;
    top: 290px;
    text-align: center;
  }
  .holder-name {
    display: inline-block;
    font-weight: 300;
    font-size: 36px;
    line-height: 1.2;
    color: var(--ink-soft);
    padding: 0 4px 2px;
    border-bottom: 2px solid var(--ink-soft);
  }
  .holder-role {
    display: block;
    margin-top: 6px;
    font-size: 21px;
    color: var(--accent);
  }
  .contact {
    position: absolute;
    left: 12px;
    top: 618px;
    font-size: 18px;
    line-height: 23px;
    color: var(--ink-soft);
    font-style: normal;
    white-space: nowrap;
  }
  .contact-gap { margin-top: 6px; }
  .contact-label { color: var(--accent); }
  .contact-email {
    display: inline-block;
    padding: 0 6px 4px 0;
    margin-left: -4px;
    padding-left: 4px;
    border-bottom: 3px solid var(--accent);
  }
</style>
</head>
<body>
<main class="stage">
  <article class="card">
    <div class="brand">Nora Quillan Casting</div>
    <svg class="brand-rules" width="327" height="8" viewBox="0 0 327 8" aria-hidden="true">
      <line x1="0" y1="1.5" x2="327" y2="1.5" stroke="var(--accent)" stroke-width="2"/>
      <line x1="6" y1="6.5" x2="327" y2="6.5" stroke="var(--rule-soft)" stroke-width="1"/>
    </svg>

    <div class="holder">
      <span class="holder-name">Your Name</span>
      <span class="holder-role">owner</span>
    </div>

    <address class="contact">
      <div>47 Thornbury Street</div>
      <div>New York, New York 10010</div>
      <div class="contact-gap"><span class="contact-label">Phone</span> - 212-738-4192</div>
      <div class="contact-email"><span class="contact-label">E-Mail</span> - Casting@noraquillan.example</div>
    </address>
  </article>
</main>
</body>
</html>
```